Seven Slides with Charts for Sales Presentation

We have the basic concept for seven important slides we need, but want to have them graphically pleasing beyond what we could do with standard charts and powerpoint. We are a software company. Attaching whiteboard versions of the slides and one graphic (slide 7). The graphics can be combined into animated slides, I will be happy to explain.

Target Market(s)

Decision Makers / Board Members for Professional Associations. For example, we are presenting to a State Association of Pharmacists next week.

Industry/Entity Type

Sales

Font styles to use
Sans Serif

Colors
33a6d7
00a990

Requirements
Must have
• Quality Graphics. I have more detail for the first slide too. You can look at http://dev.plumvessel.example for a sneak peek.
Nice to have
• Web "3.0" look and feel. Tablet / mobile friendly look.
Should not have
• Clip art or anything unprofessional.

```html
<!DOCTYPE html>
<html lang="en">
<head>
<meta charset="utf-8">
<title>Sales Presentation Slides</title>
<link rel="stylesheet" href="https://fonts.googleapis.com/css2?family=Quicksand:wght@400;500;600;700&display=swap">
<style>
  :root {
    --teal: #17ab92;
    --teal-mid: #5cc5b1;
    --teal-light: #a8e1d6;
    --blue: #33a6d7;
    --blue-light: #b7dcf1;
    --blue-soft: #7cc0e6;
    --grey: #6d6e70;
    --grey-light: #c7c8ca;
    --ink: #3c3c3e;
    --paper: #ffffff;
  }
  html, body {
    margin: 0;
    width: 1200px;
    height: 923px;
    overflow: hidden;
    background: var(--paper);
    font-family: "Quicksand", sans-serif;
  }
  .deck { position: relative; width: 1200px; height: 923px; }
  .slide {
    position: absolute;
    width: 365px;
    height: 275px;
    background: var(--paper);
    box-shadow: 0 1px 5px rgba(0,0,0,.22);
    overflow: hidden;
  }
  .slide svg { display: block; width: 365px; height: 275px; }
  .s1 { left: 27px; top: 20px; }
  .s2 { left: 415px; top: 20px; }
  .s3 { left: 805px; top: 20px; }
  .s4 { left: 27px; top: 324px; }
  .s5 { left: 415px; top: 324px; }
  .s6 { left: 805px; top: 324px; }
  .s7 { left: 415px; top: 626px; }

  text { font-family: "Quicksand", sans-serif; }
  .title { font-size: 17px; fill: var(--ink); font-weight: 500; }
  .title-white { font-size: 16px; fill: #fff; font-weight: 500; }
  .kicker { font-size: 9px; font-weight: 700; fill: var(--ink); letter-spacing: .3px; }
  .page-num { font-size: 10px; fill: #fff; font-weight: 600; }
  .person-name { font-size: 11px; font-weight: 700; fill: var(--blue); }
  .person-bio { font-size: 7.5px; fill: var(--grey); }
  .photo-label { font-size: 7.5px; fill: #fff; font-weight: 600; }
  .pct { font-size: 11px; fill: var(--grey); }
  .pct-note { font-size: 6px; fill: var(--grey); }
  .tag { font-size: 10px; fill: #fff; font-weight: 600; }
  .tag-note { font-size: 7.5px; fill: var(--blue); }
  .tag-note-teal { font-size: 7.5px; fill: var(--teal); }
  .share { font-size: 11px; font-weight: 700; }
  .share-name { font-size: 7px; }
  .center-big { font-size: 14px; font-weight: 700; fill: var(--ink); }
  .legend { font-size: 17px; font-weight: 500; }
  .card-head { font-size: 8px; fill: #fff; font-weight: 700; }
  .card-note { font-size: 4.5px; fill: var(--grey); }
  .card-pct { font-size: 6.5px; font-weight: 700; }
  .matrix-btn { font-size: 4.8px; fill: #fff; font-weight: 700; }
  .matrix-row { font-size: 6px; fill: var(--grey); font-weight: 600; }
  .bubble { font-size: 5.5px; fill: #fff; font-weight: 600; }
  .phase { font-size: 7px; fill: #fff; font-weight: 700; }
  .axis-label { font-size: 8px; fill: var(--grey); }
  .band-text { font-size: 8px; fill: #fff; }
  .time { font-size: 8px; fill: #fff; font-weight: 700; }
  .star-gold { fill: #f2b51c; }
</style>
</head>
<body>
<main class="deck">

  <!-- Slide 1: team -->
  <section class="slide s1" aria-label="Team slide">
    <svg viewBox="0 0 365 275">
      <rect class="header-band" x="0" y="0" width="365" height="108" fill="var(--teal)"/>
      <rect x="0" y="118" width="365" height="5" fill="var(--teal)"/>
      <text class="title-white" x="182.5" y="44" text-anchor="middle">Harlow Association of Rocket Scientists</text>
      <g class="team-member">
        <circle cx="59" cy="114" r="31" fill="var(--grey)" stroke="#fff" stroke-width="4"/>
        <text class="photo-label" x="59" y="106" text-anchor="middle">ADD</text>
        <text class="photo-label" x="59" y="116" text-anchor="middle">PHOTO</text>
        <text class="photo-label" x="59" y="126" text-anchor="middle">HERE</text>
        <text class="person-name" x="59" y="159" text-anchor="middle">John Doe</text>
        <text class="person-bio" x="59" y="171" text-anchor="middle">Lorem ipsum</text>
        <text class="person-bio" x="59" y="180" text-anchor="middle">dolorsit amet,</text>
        <text class="person-bio" x="59" y="189" text-anchor="middle">consectetur</text>
        <text class="person-bio" x="59" y="198" text-anchor="middle">adipiscing elit,</text>
        <text class="person-bio" x="59" y="207" text-anchor="middle">sed do</text>
      </g>
      <g class="team-member">
        <circle cx="141" cy="114" r="31" fill="var(--grey)" stroke="#fff" stroke-width="4"/>
        <text class="photo-label" x="141" y="106" text-anchor="middle">ADD</text>
        <text class="photo-label" x="141" y="116" text-anchor="middle">PHOTO</text>
        <text class="photo-label" x="141" y="126" text-anchor="middle">HERE</text>
        <text class="person-name" x="141" y="159" text-anchor="middle">John Doe</text>
        <text class="person-bio" x="141" y="171" text-anchor="middle">Lorem ipsum</text>
        <text class="person-bio" x="141" y="180" text-anchor="middle">dolorsit amet,</text>
        <text class="person-bio" x="141" y="189" text-anchor="middle">consectetur</text>
        <text class="person-bio" x="141" y="198" text-anchor="middle">adipiscing elit,</text>
        <text class="person-bio" x="141" y="207" text-anchor="middle">sed do</text>
      </g>
      <g class="team-member">
        <circle cx="223" cy="114" r="31" fill="var(--grey)" stroke="#fff" stroke-width="4"/>
        <text class="photo-label" x="223" y="106" text-anchor="middle">ADD</text>
        <text class="photo-label" x="223" y="116" text-anchor="middle">PHOTO</text>
        <text class="photo-label" x="223" y="126" text-anchor="middle">HERE</text>
        <text class="person-name" x="223" y="159" text-anchor="middle">John Doe</text>
        <text class="person-bio" x="223" y="171" text-anchor="middle">Lorem ipsum</text>
        <text class="person-bio" x="223" y="180" text-anchor="middle">dolorsit amet,</text>
        <text class="person-bio" x="223" y="189" text-anchor="middle">consectetur</text>
        <text class="person-bio" x="223" y="198" text-anchor="middle">adipiscing elit,</text>
        <text class="person-bio" x="223" y="207" text-anchor="middle">sed do</text>
      </g>
      <g class="team-member">
        <circle cx="305" cy="114" r="31" fill="var(--grey)" stroke="#fff" stroke-width="4"/>
        <text class="photo-label" x="305" y="106" text-anchor="middle">ADD</text>
        <text class="photo-label" x="305" y="116" text-anchor="middle">PHOTO</text>
        <text class="photo-label" x="305" y="126" text-anchor="middle">HERE</text>
        <text class="person-name" x="305" y="159" text-anchor="middle">John Doe</text>
        <text class="person-bio" x="305" y="171" text-anchor="middle">Lorem ipsum</text>
        <text class="person-bio" x="305" y="180" text-anchor="middle">dolorsit amet,</text>
        <text class="person-bio" x="305" y="189" text-anchor="middle">consectetur</text>
        <text class="person-bio" x="305" y="198" text-anchor="middle">adipiscing elit,</text>
        <text class="person-bio" x="305" y="207" text-anchor="middle">sed do</text>
      </g>
      <rect x="338" y="249" width="20" height="20" fill="var(--teal)"/>
      <text class="page-num" x="348" y="263" text-anchor="middle">1</text>
    </svg>
  </section>

  <!-- Slide 2: revenue allocation -->
  <section class="slide s2" aria-label="Revenue Allocation slide">
    <svg viewBox="0 0 365 275">
      <rect x="38" y="0" width="48" height="62" fill="var(--teal)"/>
      <line x1="38" y1="70" x2="270" y2="70" stroke="var(--teal)" stroke-width="1"/>
      <g class="icon-growth" fill="none" stroke="#fff" stroke-width="2">
        <rect x="48" y="40" width="4" height="8" fill="#fff" stroke="none"/>
        <rect x="55" y="35" width="4" height="13" fill="#fff" stroke="none"/>
        <rect x="62" y="30" width="4" height="18" fill="#fff" stroke="none"/>
        <rect x="69" y="26" width="4" height="22" fill="#fff" stroke="none"/>
        <polyline points="48,32 58,24 64,28 76,17"/>
        <polyline points="70,17 76,17 76,23"/>
      </g>
      <text class="title" x="104" y="60">Revenue Allocation</text>

      <rect x="249" y="85" width="57" height="171" fill="var(--blue)"/>
      <rect x="249" y="85" width="57" height="38" fill="var(--blue-light)"/>
      <rect x="249" y="123" width="57" height="9" fill="var(--blue-soft)"/>
      <rect x="249" y="132" width="57" height="6" fill="#5bb3e0"/>

      <g stroke="var(--grey-light)" stroke-width="1" fill="none">
        <polyline points="140,96 144,96 144,142 140,142"/>
        <polyline points="154,112 178,112 178,99 249,99"/>
        <polyline points="154,178 210,178 210,127 249,127"/>
        <polyline points="140,221 144,221 144,270"/>
        <polyline points="154,249 228,249 228,135 249,135"/>
        <line x1="178" y1="122" x2="249" y2="122"/>
      </g>
      <rect x="147" y="107" width="5" height="10" fill="var(--teal)"/>
      <rect x="147" y="175" width="5" height="5" fill="var(--teal)"/>
      <rect x="147" y="269" width="5" height="3" fill="var(--teal)"/>

      <text class="pct" x="138" y="106" text-anchor="end">25%</text>
      <text class="pct-note" x="138" y="115" text-anchor="end">Software license -</text>
      <text class="pct-note" x="138" y="123" text-anchor="end">Accounting -</text>
      <text class="pct-note" x="138" y="131" text-anchor="end">Administration -</text>
      <text class="pct" x="138" y="171" text-anchor="end">10%</text>
      <text class="pct-note" x="138" y="181" text-anchor="end">Advertising</text>
      <text class="pct" x="138" y="236" text-anchor="end">3% - 5%</text>
      <text class="pct-note" x="138" y="245" text-anchor="end">Credit Card Transaction Fees -</text>
      <text class="pct-note" x="138" y="253" text-anchor="end">Association Specific Expenses -</text>

      <rect x="338" y="249" width="20" height="20" fill="var(--teal)"/>
      <text class="page-num" x="348" y="263" text-anchor="middle">2</text>
    </svg>
  </section>

  <!-- Slide 3: proceeds -->
  <section class="slide s3" aria-label="Proceed slide">
    <svg viewBox="0 0 365 275">
      <rect x="38" y="0" width="48" height="62" fill="var(--teal)"/>
      <line x1="38" y1="70" x2="270" y2="70" stroke="var(--teal)" stroke-width="1"/>
      <polygon points="53,22 53,48 74,35" fill="none" stroke="#fff" stroke-width="2.5" stroke-linejoin="round"/>
      <text class="title" x="104" y="60">Proceed</text>

      <line x1="31" y1="148" x2="31" y2="249" stroke="var(--ink)" stroke-width="2"/>
      <polygon points="226,164 300,164 324,198 300,232 226,232" fill="var(--teal)"/>
      <polygon points="34,164 240,164 264,198 240,232 34,232" fill="var(--blue)"/>

      <line x1="109" y1="115" x2="109" y2="164" stroke="var(--blue)" stroke-width="1"/>
      <rect x="108" y="94" width="47" height="21" fill="var(--blue)"/>
      <text class="tag" x="131.5" y="108" text-anchor="middle">75 %</text>
      <text class="tag-note" x="114" y="127">Paid to</text>
      <text class="tag-note" x="114" y="137">Association</text>

      <line x1="244" y1="115" x2="244" y2="164" stroke="var(--teal)" stroke-width="1"/>
      <rect x="243" y="94" width="47" height="21" fill="var(--teal)"/>
      <text class="tag" x="266.5" y="108" text-anchor="middle">75 %</text>
      <text class="tag-note-teal" x="249" y="127">HA Contribution to</text>
      <text class="tag-note-teal" x="249" y="137">Instructor Payout Pool</text>

      <rect x="338" y="249" width="20" height="20" fill="var(--teal)"/>
      <text class="page-num" x="348" y="263" text-anchor="middle">3</text>
    </svg>
  </section>

  <!-- Slide 4: instructor payout pool -->
  <section class="slide s4" aria-label="Instructor Payout Pool slide">
    <svg viewBox="0 0 365 275">
      <rect x="38" y="0" width="48" height="62" fill="var(--teal)"/>
      <line x1="38" y1="70" x2="270" y2="70" stroke="var(--teal)" stroke-width="1"/>
      <g class="icon-cash" fill="none" stroke="#fff" stroke-width="1.8">
        <rect x="48" y="20" width="22" height="14" transform="rotate(-20 59 27)"/>
        <rect x="52" y="28" width="22" height="14" transform="rotate(-8 63 35)"/>
        <rect x="54" y="36" width="24" height="14" fill="var(--teal)"/>
        <circle cx="66" cy="43" r="3.5"/>
      </g>
      <text class="title" x="104" y="60">Instructor Payout Pool</text>

      <g transform="rotate(-90 175 179)" fill="none" stroke-width="20">
        <circle cx="175" cy="179" r="46" stroke="var(--teal)" stroke-dasharray="96.3 289"/>
        <circle cx="175" cy="179" r="46" stroke="var(--grey-light)" stroke-dasharray="96.3 289" stroke-dashoffset="-96.3"/>
        <circle cx="175" cy="179" r="46" stroke="var(--blue)" stroke-dasharray="96.3 289" stroke-dashoffset="-192.6"/>
      </g>
      <text class="center-big" x="175" y="177" text-anchor="middle" style="font-size:11px;font-weight:600">YEARS</text>
      <text class="center-big" x="175" y="193" text-anchor="middle" style="font-size:12px;font-weight:600">20XX</text>

      <text class="share-name" x="108" y="125" fill="var(--blue)">Sally</text>
      <text class="share" x="108" y="138" fill="var(--blue)">33%</text>
      <line x1="106" y1="141" x2="128" y2="141" stroke="var(--blue)"/>
      <text class="share-name" x="243" y="125" fill="var(--teal)">Johnny</text>
      <text class="share" x="243" y="138" fill="var(--teal)">33%</text>
      <line x1="241" y1="141" x2="263" y2="141" stroke="var(--teal)"/>
      <line x1="191" y1="236" x2="213" y2="236" stroke="var(--grey)"/>
      <text class="share" x="193" y="249" fill="var(--grey)">33%</text>
      <text class="share-name" x="192" y="257" fill="var(--grey)">George</text>

      <rect x="338" y="249" width="20" height="20" fill="var(--teal)"/>
      <text class="page-num" x="348" y="263" text-anchor="middle">4</text>
    </svg>
  </section>

  <!-- Slide 5: instructor ratings -->
  <section class="slide s5" aria-label="Instructor ratings slide">
    <svg viewBox="0 0 365 275">
      <path d="M195 128 A78 78 0 1 1 117 50" fill="none" stroke="var(--blue)" stroke-width="22"/>
      <path d="M117 76 A52 52 0 0 0 72 154" fill="none" stroke="var(--teal)" stroke-width="14"/>
      <path d="M117 90 A38 38 0 0 0 90 101" fill="none" stroke="var(--grey)" stroke-width="6"/>
      <circle cx="117" cy="128" r="25" fill="#fff" stroke="var(--ink)" stroke-width="1.5"/>
      <text class="center-big" x="117" y="133" text-anchor="middle">100%</text>

      <text class="legend" x="140" y="36" fill="var(--blue)">Sally</text>
      <text class="legend" x="140" y="54" fill="var(--teal)">George</text>
      <text class="legend" x="140" y="72" fill="var(--grey)">Johnny</text>

      <g class="rating-card">
        <rect x="268" y="20" width="54" height="77" fill="none" stroke="var(--blue)" stroke-dasharray="2 1.5"/>
        <rect x="272" y="24" width="46" height="11" fill="var(--blue)"/>
        <text class="card-head" x="295" y="32.5" text-anchor="middle">Sally</text>
        <circle cx="295" cy="50" r="9" fill="none" stroke="var(--grey-light)" stroke-width="3"/>
        <circle cx="295" cy="50" r="9" fill="none" stroke="var(--blue)" stroke-width="3" stroke-dasharray="39.6 56.5" transform="rotate(-90 295 50)"/>
        <text class="card-pct" x="295" y="52.5" text-anchor="middle" fill="var(--blue)">70%</text>
        <text class="star-gold" x="295" y="69" text-anchor="middle" style="font-size:7px">★★★★★</text>
        <text class="card-note" x="295" y="76" text-anchor="middle">Engaging</text>
        <text class="card-note" x="295" y="82" text-anchor="middle">Timely</text>
        <text class="card-note" x="295" y="88" text-anchor="middle">Highly Relevant</text>
      </g>
      <g class="rating-card">
        <rect x="268" y="105" width="54" height="73" fill="none" stroke="var(--teal)" stroke-dasharray="2 1.5"/>
        <rect x="272" y="109" width="46" height="11" fill="var(--teal)"/>
        <text class="card-head" x="295" y="117.5" text-anchor="middle">George</text>
        <circle cx="295" cy="135" r="9" fill="none" stroke="var(--grey-light)" stroke-width="3"/>
        <circle cx="295" cy="135" r="9" fill="none" stroke="var(--teal)" stroke-width="3" stroke-dasharray="14.1 56.5" transform="rotate(-90 295 135)"/>
        <text class="card-pct" x="295" y="137.5" text-anchor="middle" fill="var(--teal)">25%</text>
        <text class="star-gold" x="295" y="154" text-anchor="middle" style="font-size:7px">★★★</text>
        <text class="card-note" x="295" y="162" text-anchor="middle">Entertaining</text>
        <text class="card-note" x="295" y="168" text-anchor="middle">Often</text>
      </g>
      <g class="rating-card">
        <rect x="268" y="186" width="54" height="63" fill="none" stroke="var(--grey)" stroke-dasharray="2 1.5"/>
        <rect x="272" y="190" width="46" height="11" fill="var(--grey)"/>
        <text class="card-head" x="295" y="198.5" text-anchor="middle">Johnny</text>
        <circle cx="295" cy="216" r="9" fill="none" stroke="var(--grey-light)" stroke-width="3"/>
        <circle cx="295" cy="216" r="9" fill="none" stroke="var(--grey)" stroke-width="3" stroke-dasharray="2.8 56.5" transform="rotate(-90 295 216)"/>
        <text class="card-pct" x="295" y="218.5" text-anchor="middle" fill="var(--grey)">5%</text>
        <text class="star-gold" x="295" y="237" text-anchor="middle" style="font-size:7px">★★</text>
      </g>

      <rect x="338" y="249" width="20" height="20" fill="var(--teal)"/>
      <text class="page-num" x="348" y="263" text-anchor="middle">5</text>
    </svg>
  </section>

  <!-- Slide 7: quality control matrix -->
  <section class="slide s6" aria-label="Quality Control Matrix slide">
    <svg viewBox="0 0 365 275">
      <rect x="38" y="0" width="48" height="62" fill="var(--teal)"/>
      <line x1="38" y1="70" x2="270" y2="70" stroke="var(--teal)" stroke-width="1"/>
      <g class="icon-monitor" fill="none" stroke="#fff" stroke-width="1.8">
        <rect x="47" y="22" width="30" height="21"/>
        <line x1="62" y1="43" x2="62" y2="49"/>
        <line x1="55" y1="49" x2="69" y2="49"/>
        <polyline points="51,38 57,32 62,35 72,26"/>
      </g>
      <text class="kicker" x="104" y="40">VELTRANA</text>
      <text class="title" x="104" y="60">Quality Control Matrix</text>

      <g stroke="var(--teal-light)" stroke-width="1">
        <line x1="58" y1="145" x2="330" y2="145"/>
        <line x1="58" y1="155" x2="330" y2="155"/>
        <line x1="58" y1="170" x2="330" y2="170"/>
        <line x1="58" y1="182" x2="330" y2="182"/>
        <line x1="58" y1="197" x2="330" y2="197"/>
        <line x1="58" y1="210" x2="330" y2="210"/>
      </g>
      <text class="matrix-row" x="24" y="157">PUBLISHER</text>
      <text class="matrix-row" x="24" y="184">INSTRUCTOR</text>
      <text class="matrix-row" x="24" y="212">LESSON</text>

      <g class="matrix-step">
        <line x1="102" y1="128" x2="102" y2="155" stroke="var(--grey)"/>
        <circle cx="102" cy="155" r="4" fill="var(--blue)" stroke="#fff" stroke-width="1.2"/>
        <rect x="77" y="101" width="50" height="27" rx="2" fill="var(--blue)"/>
        <polygon points="98,128 106,128 102,133" fill="var(--blue)"/>
        <text class="matrix-btn" x="102" y="113" text-anchor="middle">APPROVE</text>
        <text class="matrix-btn" x="102" y="120" text-anchor="middle">EVERYTHING</text>
      </g>
      <g class="matrix-step">
        <line x1="164" y1="128" x2="164" y2="182" stroke="var(--grey)"/>
        <circle cx="164" cy="182" r="4" fill="var(--blue)" stroke="#fff" stroke-width="1.2"/>
        <rect x="139" y="101" width="50" height="27" rx="2" fill="var(--blue)"/>
        <polygon points="160,128 168,128 164,133" fill="var(--blue)"/>
        <text class="matrix-btn" x="164" y="110" text-anchor="middle">AUTO</text>
        <text class="matrix-btn" x="164" y="117" text-anchor="middle">APPROVE BY</text>
        <text class="matrix-btn" x="164" y="124" text-anchor="middle">REQUIREMENTS</text>
      </g>
      <g class="matrix-step">
        <line x1="226" y1="128" x2="226" y2="210" stroke="var(--grey)"/>
        <circle cx="226" cy="210" r="4" fill="var(--blue)" stroke="#fff" stroke-width="1.2"/>
        <rect x="201" y="101" width="50" height="27" rx="2" fill="var(--blue)"/>
        <polygon points="222,128 230,128 226,133" fill="var(--blue)"/>
        <text class="matrix-btn" x="226" y="110" text-anchor="middle">SUGGEST</text>
        <text class="matrix-btn" x="226" y="117" text-anchor="middle">APPROVAL BY</text>
        <text class="matrix-btn" x="226" y="124" text-anchor="middle">REQUIREMENT</text>
      </g>
      <g class="matrix-step">
        <rect x="272" y="101" width="50" height="27" rx="2" fill="var(--blue)"/>
        <polygon points="293,128 301,128 297,133" fill="var(--blue)"/>
        <text class="matrix-btn" x="297" y="113" text-anchor="middle">APPROVE</text>
        <text class="matrix-btn" x="297" y="120" text-anchor="middle">MANUALLY</text>
      </g>

      <rect x="338" y="249" width="20" height="20" fill="var(--teal)"/>
      <text class="page-num" x="348" y="263" text-anchor="middle">7</text>
    </svg>
  </section>

  <!-- Slide: quality of lessons over time -->
  <section class="slide s7" aria-label="Quality of lessons over time slide">
    <svg viewBox="0 0 365 275">
      <rect x="0" y="192" width="365" height="83" fill="var(--teal)"/>

      <polygon points="63,191 162,191 162,139" fill="var(--teal)"/>
      <polygon points="162,191 249,191 249,93 162,139" fill="var(--teal-mid)"/>
      <polygon points="249,191 333,191 333,55 249,93" fill="var(--teal-light)"/>

      <g stroke="var(--grey)" stroke-width="1" stroke-dasharray="3 2">
        <line x1="162" y1="113" x2="162" y2="191"/>
        <line x1="249" y1="66" x2="249" y2="191"/>
      </g>
      <circle cx="162" cy="89" r="24" fill="var(--grey)"/>
      <text class="bubble" x="162" y="88" text-anchor="middle">Competition</text>
      <text class="bubble" x="162" y="95" text-anchor="middle">Ensues</text>
      <circle cx="249" cy="42" r="24" fill="var(--grey)"/>
      <text class="bubble" x="249" y="41" text-anchor="middle">Quality</text>
      <text class="bubble" x="249" y="48" text-anchor="middle">Saturation</text>

      <rect x="114" y="170" width="38" height="13" fill="var(--teal)" stroke="#fff" stroke-width=".8"/>
      <text class="phase" x="133" y="179.5" text-anchor="middle">PHASE 1</text>
      <rect x="186" y="149" width="38" height="13" fill="var(--teal)" stroke="#fff" stroke-width=".8"/>
      <text class="phase" x="205" y="158.5" text-anchor="middle">PHASE 2</text>
      <rect x="269" y="117" width="38" height="13" fill="var(--teal)" stroke="#fff" stroke-width=".8"/>
      <text class="phase" x="288" y="126.5" text-anchor="middle">PHASE 3</text>

      <line x1="47" y1="185" x2="47" y2="52" stroke="var(--blue)" stroke-width="1.5"/>
      <polygon points="43,54 51,54 47,46" fill="var(--blue)"/>
      <text class="axis-label" x="43" y="100" text-anchor="end">Quality</text>
      <text class="axis-label" x="43" y="110" text-anchor="end">of Lessons</text>

      <rect x="47" y="188" width="304" height="6" fill="var(--blue)"/>
      <polygon points="350,184 360,191 350,198" fill="var(--blue)"/>
      <circle cx="47" cy="191" r="11" fill="var(--blue)" stroke="#fff" stroke-width="2"/>
      <circle cx="47" cy="191" r="6" fill="none" stroke="#fff" stroke-width="1.3"/>
      <polyline points="47,187.5 47,191 50,192.5" fill="none" stroke="#fff" stroke-width="1.2"/>
      <text class="time" x="47" y="216" text-anchor="middle">TIME</text>

      <text class="band-text" x="131" y="214" text-anchor="middle">Higher</text>
      <text class="band-text" x="131" y="224" text-anchor="middle">Convenience</text>
      <text class="band-text" x="131" y="234" text-anchor="middle">Current Standards</text>
      <text class="band-text" x="208" y="214" text-anchor="middle">Competition</text>
      <text class="band-text" x="208" y="224" text-anchor="middle">Drives Quality</text>
      <text class="band-text" x="208" y="234" text-anchor="middle">Improvements</text>
      <text class="band-text" x="296" y="214" text-anchor="middle">Diversification</text>
      <text class="band-text" x="296" y="224" text-anchor="middle">+</text>
      <text class="band-text" x="296" y="234" text-anchor="middle">Specialization</text>

      <rect x="338" y="249" width="20" height="20" fill="#fff" stroke="var(--grey-light)"/>
      <text class="page-num" x="348" y="263" text-anchor="middle" style="fill:var(--teal)">5</text>
    </svg>
  </section>

</main>
</body>
</html>
```